The Burrow On Maple "Neighborhood Tavern" - Menu Re-Design

HI,
I am a restaurant owner in Los Angeles, CA and I need to overhaul my food & drink menus. I would like something more creative than what I currently have. Please keep in mind that this is a neighborhood bar & tavern on the Maple Row in Los Angeles. We are not a fine dining establishment, diner or sports bar. Please view our website to get a feel for the current brand identity http://www.theburrowonmaple.com
I will upload our current menu which is simple and our previous design which was more involved. I would like this new menu design to be fun and engage our customers to order more food and drink.
Lastly I would like to be able to update the content easily.
Additional Info based on designer questions added 8-20-15:
Preferred size is 8.5x14 in. / legal size.
I do not want food pics on the menu but artistic food and drink drawings are okay.
The link below has logo files and the previous menu file in AI.
https://files.quorvashare.com/u/517608/Menu%20Re-Design%20Reference%20Folder.zip
Industry/Entity Type
Restaurant
Requirements
Must have
- be editable by my staff which has basic AI knowledge
Should not have
- food photos

```html
<!DOCTYPE html>
<html lang="en">
<head>
<meta charset="utf-8">
<title>The Burrow On Maple – Menu</title>
<link href="https://fonts.googleapis.com/css2?family=Roboto+Slab:wght@700;900&family=Roboto+Condensed:wght@400;700&display=swap" rel="stylesheet">
<style>
  :root{
    --red:#9b1c25;
    --ink:#3b3b3b;
    --paper:#ffffff;
    --muted:#5a5a5a;
  }
  *{box-sizing:border-box;margin:0;padding:0}
  html,body{width:729px;height:1200px;overflow:hidden;background:var(--paper)}
  body{position:relative;font-family:"Roboto Condensed",Arial,sans-serif;color:var(--ink)}
  .block{position:absolute}
  .brand{left:22px;top:22px;display:flex;align-items:center;gap:8px}
  .brand-mark{width:14px;height:14px;background:var(--red)}
  .brand-name{font-family:"Roboto Slab",Georgia,serif;font-weight:900;font-size:21px;color:var(--red);line-height:1.05;width:150px}
  .hours{left:215px;top:12px;width:280px;text-align:center;font-weight:700;font-size:11.5px;line-height:1.5;text-transform:uppercase;letter-spacing:.5px}
  .hours strong{color:var(--red)}

  .section-title{font-family:"Roboto Slab",Georgia,serif;font-weight:900;text-transform:uppercase;color:var(--ink);text-align:center;border-top:2px solid var(--red);border-bottom:2px solid var(--red);padding:5px 0;font-size:22px;letter-spacing:.5px}
  .band{background:var(--red);color:#fff;border:none}

  .item{margin-bottom:9px;text-align:center}
  .item h3{font-family:"Roboto Slab",Georgia,serif;font-weight:900;font-size:15px;line-height:1.15;text-transform:none}
  .item h3.red{color:var(--red);text-transform:uppercase}
  .item p{font-size:11px;line-height:1.3;color:var(--muted)}
  .item .note{font-style:italic}
  .price{font-weight:700;color:var(--ink)}

  .sandwiches{left:505px;top:0;width:224px;height:615px;border-left:2px solid var(--red);padding:20px 12px 0}
  .sandwiches .section-title{margin:0 -12px 10px}
  .sandwiches .item{margin-bottom:7px}

  .barfood{left:10px;top:98px;width:485px;height:520px}
  .barfood .cols{display:flex;gap:14px;margin-top:12px}
  .barfood .col{flex:1}
  .barfood .item{margin-bottom:11px}
  .barfood .right-col{border:2px solid var(--red);padding:8px 6px 0}

  .salads{left:10px;top:630px;width:178px;border:2px solid var(--red);padding:0 8px 6px}
  .salads .section-title{margin:0 -8px 10px}
  .salads .item{margin-bottom:12px}

  .flatbreads{left:200px;top:640px;width:519px;height:420px}
  .flatbreads .cols{display:flex;gap:16px;margin-top:12px}
  .flatbreads .col{flex:1}
  .flatbreads .item{margin-bottom:14px}
  .flatbreads .item h3{font-size:17px}
  .flatbreads .mid{text-align:center;font-weight:700;font-size:13px;color:var(--red);margin:4px 0 10px}
  .flatbreads .gf{text-align:center;font-size:11px;font-weight:700}

  .happy-offer{left:370px;top:1070px;width:350px;text-align:center;font-family:"Roboto Slab",Georgia,serif;font-weight:900;font-size:13px;color:var(--red);text-transform:uppercase}
  .events{left:10px;top:1098px;width:500px;background:var(--red);color:#fff;text-align:center;font-weight:700;font-size:12.5px;padding:5px 0;text-transform:uppercase;letter-spacing:.5px}
  .events-site{left:10px;top:1124px;width:500px;text-align:center;font-size:11px;font-weight:700;color:var(--muted)}
  .happy-hour{left:0;top:1160px;width:729px;text-align:center;font-family:"Roboto Slab",Georgia,serif;font-weight:900;font-size:12.5px;color:var(--ink);text-transform:uppercase;border-top:2px solid var(--red);padding-top:10px}
</style>
</head>
<body>

<header class="block brand">
  <span class="brand-mark"></span>
  <span class="brand-name">The Burrow On Maple</span>
</header>

<div class="block hours">
  <strong>Hours:</strong> Mon – Fri 5pm – 2am<br>
  Sat 3pm – 2am<br>
  Sun 12pm – 2am<br>
  <strong>DJ Friday &amp; Saturday</strong><br>
  10pm – 2am
</div>

<section class="block sandwiches">
  <h2 class="section-title band">Sandwiches</h2>
  <div class="item"><h3>Breakfast Sandwich</h3><p>Bacon, Gruyere, Fried Egg <span class="price">10</span><br>+ Avocado 2, Tomato 1</p></div>
  <div class="item"><h3 class="red">Burrow Burger</h3><p>Grass Fed Beef, Brindlecreek Cheddar, Arugula, Red Onion, House Sauce, Brioche Bun <span class="price">12</span></p></div>
  <div class="item"><h3>Sunny-Side-Up Burger</h3><p>Grass Fed Beef, Fried Egg, Brindlecreek Sharp Cheddar Cheese <span class="price">12</span></p></div>
  <div class="item"><h3 class="red">BBQ Cheeseburger</h3><p>Grass Fed Beef, Housemade Bacon BBQ Sauce, Sharp Cheddar, Onion Rings <span class="price">13</span></p></div>
  <div class="item"><h3>Deluxe Burger</h3><p>Grass Fed Beef, Onion Rings, Fried Egg, Tomato Jam, Smoked Ketchup, Brioche Bun <span class="price">14</span></p></div>
  <div class="item"><h3 class="red">Bistro Steak Sandwich</h3><p>Flat Iron Steak, Gruyere Cheese, Caramelized Onions, Creole Mustard, Rosemary <span class="price">14</span></p></div>
  <div class="item"><h3>Veggie Burger</h3><p>Black Beans, Roasted Corn, Roasted Red Peppers, Spinach, Pepper Jack, Avocado, Tomato <span class="price">12</span></p></div>
  <div class="item"><h3 class="red">Crispy Chicken Sandwich</h3><p>Fried Chicken, Pickled Cucumber Jalapeno Slaw, Malt Vinegar Aioli <span class="price">12</span></p></div>
  <div class="item"><h3>Smoked Turkey Sandwich</h3><p>House Smoked Turkey, Bacon, Chipotle Aioli, Pepper Jack Cheese, Avocado <span class="price">13</span><br>+ Fries for 3, Truffle Fries 4, Side Salad 4, Gluten Free Bread 2</p></div>
</section>

<section class="block barfood">
  <h2 class="section-title">Bar Food, Sides &amp; Extras</h2>
  <div class="cols">
    <div class="col">
      <div class="item"><h3>Edamame <span class="price" style="font-family:'Roboto Condensed',sans-serif;font-size:11px">Sea Salt 4</span></h3></div>
      <div class="item"><h3>Deviled Eggs <span class="price">6</span></h3></div>
      <div class="item"><h3 class="red">Crispy Hot Wings</h3><p>Spicy or BBQ, served w/ Ranch or Blue Cheese <span class="price">8</span></p></div>
      <div class="item"><h3>Bacon Wrapped Dates</h3><p>Medjool Dates, Halden Blue Cheese &amp; Smoked Bacon <span class="price">10</span></p></div>
      <div class="item"><h3>Mac Daddy</h3><p>Creamy Mac &amp; Cheese With Prosciutto, English Peas &amp; Parmesan <span class="price">10</span></p></div>
      <div class="item"><h3 class="red">Brussels Sprouts</h3><p>Smoked Almond Vinaigrette, Bacon Jus, Arugula, Parmesan Cheese <span class="price">9</span></p><p class="note">also Available without Bacon Jus</p></div>
      <div class="item"><h3>Homemade Chocolate Chip Cookies <span class="price">2 for 3</span></h3></div>
    </div>
    <div class="col right-col">
      <div class="item"><h3 class="red">Hand Cut Shoestring Fries</h3><p>Regular, Sweet Potato or Truffle &amp; Truffle Fries Add 2</p></div>
      <div class="item"><h3>Poutine</h3><p>Shoestring Fries, Housemade Chicken Gravy, White Cheddar Cheese Curds <span class="price">10</span></p></div>
      <div class="item"><h3>Grilled Artichoke</h3><p>Lemon Garlic Aioli <span class="price">11</span></p></div>
      <div class="item"><h3>Angry Mac Bites</h3><p>Green Chile &amp; Chipotle Aioli <span class="price">6</span></p></div>
      <div class="item"><h3 class="red">Hummus Plate</h3><p>Chickpea Hummus, Feta Cheese, Paprika Oil, Grilled Pita <span class="price">8</span></p></div>
      <div class="item"><h3>German Pretzel</h3><p>Loaded w/ Cheese, Bacon Bits, served w/ Spicy Mustard &amp; Ranch <span class="price">7</span></p></div>
      <div class="item"><h3 class="red">Truffle Mac</h3><p>Creamy Mac &amp; Cheese w/ Gruyere &amp; Cheddar Cheese, Wild Mushrooms, Truffle Oil <span class="price">12</span></p></div>
    </div>
  </div>
</section>

<section class="block salads">
  <h2 class="section-title band">Salads</h2>
  <div class="item"><h3>Kale Salad</h3><p>Baby Kale, Radicchio, Golden Raisins, Herbed Breadcrumbs, Shaved Parmesan, Lemon Vinaigrette <span class="price">10</span></p></div>
  <div class="item"><h3 class="red">Chop Salad</h3><p>Tomatoes, Grilled Corn, Cucumbers, Bacon, Red Onions, Blue Cheese, Champagne Vinaigrette <span class="price">10</span></p></div>
  <div class="item"><h3>Caesar Salad</h3><p>Romaine Lettuce, Shaved Parmesan, Garlic Croutons, Caesar Dressing <span class="price">10</span></p></div>
  <div class="item"><p><strong>+ Protein:</strong> Smoked Turkey 5, Grilled Chicken Breast 6, Flat Iron Steak 7</p></div>
</section>

<section class="block flatbreads">
  <h2 class="section-title">Flat Breads</h2>
  <div class="mid">— 13 —</div>
  <div class="cols">
    <div class="col">
      <div class="item"><h3>Veggie</h3><p>Smoked Mozzarella, Zucchini, Oven Roasted Tomatoes, Brussels Sprouts, Grilled Red Onions</p></div>
      <div class="item"><h3 class="red">BBQ Chicken</h3><p>Mozzarella, Red Onion, Cilantro, BBQ Sauce</p></div>
      <div class="item"><h3>Wild Mushroom &amp; Goat Cheese</h3><p>Bianca Sauce, Fresh Herbs</p></div>
    </div>
    <div class="col">
      <div class="item"><h3 class="red">Margherita</h3><p>Fresh Mozzarella, Tomatoes, Basil, Pizza Sauce</p></div>
      <div class="item"><h3>Prosciutto</h3><p>Sliced Prosciutto, Medjool Dates, Goat Cheese, Arugula, Fig Balsamic Glaze</p></div>
      <div class="item"><h3 class="red">Pepperoni</h3><p>Pepperoni, Mozzarella Cheese, Pizza Sauce</p></div>
    </div>
  </div>
  <p class="gf">Gluten Free Crust + 3</p>
</section>

<div class="block happy-offer">Take $2 off during happy hour, Mon – Fri 5-7pm</div>
<div class="block events">Book your next event here! Info@theburrowonmaple.com</div>
<div class="block events-site">www.theburrowonmaple.com</div>
<footer class="block happy-hour">Happy Hour $2 off all beer &amp; signature cocktails, $3 off wine by the glass, well drinks $4</footer>

</body>
</html>
```